Business Card Design

We just need these details on one side of card and logo on the other.

Industry/Entity Type

Business

Contact Information for Business Card

Colette Marsh | Artist
87 Tillbrook Lane
Dunmore Heights Vic 3172
# 0418 207 913 | 03 9386 2417
colette@colettemarsh-example.com
colettesstudio-example.com.au

```html
<!DOCTYPE html>
<html lang="en">
<head>
<meta charset="utf-8">
<title>Colette's Studio – Business Cards</title>
<link href="https://fonts.googleapis.com/css2?family=Quicksand:wght@400;500&display=swap" rel="stylesheet">
<style>
  :root {
    --backdrop: #3a3a3a;
    --card-dark: #0d0d0d;
    --card-mid: #262626;
    --band: #2f2f2f;
    --ink: #ffffff;
    --ink-soft: #d6d6d6;
    --silver: #cfcfcf;
    --silver-dark: #7a7a7a;
  }
  * { box-sizing: border-box; margin: 0; padding: 0; }
  html, body { width: 1200px; height: 800px; overflow: hidden; }
  body {
    background: var(--backdrop);
    font-family: "Quicksand", sans-serif;
    color: var(--ink);
    position: relative;
  }
  .card {
    position: absolute;
    width: 500px;
    height: 306px;
    overflow: hidden;
    box-shadow: 0 10px 26px rgba(0,0,0,.45);
    background:
      radial-gradient(ellipse at 45% 40%, var(--card-mid) 0%, var(--card-dark) 75%);
  }
  .card--front { left: 90px; top: 110px; }
  .card--back  { left: 610px; top: 384px; }

  /* front */
  .card__edge {
    position: absolute; left: 0; right: 0; height: 14px;
    background: linear-gradient(var(--card-dark), #1a1a1a);
  }
  .card__edge--top { top: 0; }
  .card__edge--bottom { bottom: 0; }
  .logo-band {
    position: absolute; left: 14px; top: 30px; width: 426px; height: 100px;
    background: linear-gradient(90deg, #1c1c1c, var(--band) 50%, #1c1c1c);
  }
  .brand {
    position: absolute; white-space: nowrap; font-weight: 400;
    color: var(--ink); letter-spacing: .5px;
  }
  .card--front .brand { left: 26px; top: 38px; font-size: 46px; }
  .tagline {
    position: absolute; white-space: nowrap;
    font-size: 12.5px; letter-spacing: 2.6px; color: var(--ink);
  }
  .card--front .tagline { left: 170px; top: 110px; }
  .holder {
    position: absolute; left: 22px; top: 146px;
    font-size: 12.5px; letter-spacing: 2.6px; font-weight: 500;
  }
  .contact {
    position: absolute; left: 22px; top: 172px;
    list-style: none; font-size: 10.5px; line-height: 15px; color: var(--ink-soft);
  }
  .birds {
    position: absolute; left: 300px; top: 170px; width: 170px; height: 70px;
    background: radial-gradient(ellipse, rgba(0,0,0,.35), transparent 70%);
  }

  /* back */
  .rules { position: absolute; left: 0; top: 0; }
  .card--back .brand { left: 0; right: 0; text-align: center; top: 100px; font-size: 50px; }
  .card--back .tagline { left: 0; right: 0; text-align: center; top: 172px; font-size: 13px; }
  .card--back .birds { left: 360px; top: 30px; width: 120px; height: 60px; }
</style>
</head>
<body>

<section class="card card--front" aria-label="Business card front">
  <div class="card__edge card__edge--top"></div>
  <div class="logo-band"></div>
  <div class="brand">Colette's Studio</div>
  <div class="tagline">STUDIO · CAFE · GALLERY</div>
  <div class="holder">COLETTE MARSH | ARTIST</div>
  <ul class="contact">
    <li>87 TILLBROOK LANE DUNMORE HEIGHTS VIC 3172</li>
    <li># 0418 207 913</li>
    <li>03 9386 2417</li>
    <li>colette@colettemarsh-example.com</li>
    <li>colettesstudio-example.com.au</li>
  </ul>
  <div class="birds" role="img" aria-label="Faint flock of birds in flight"></div>
  <div class="card__edge card__edge--bottom"></div>
</section>

<section class="card card--back" aria-label="Business card back">
  <svg class="rules" width="500" height="306" viewBox="0 0 500 306" aria-hidden="true">
    <defs>
      <linearGradient id="silver" x1="0" x2="1">
        <stop offset="0" stop-color="var(--silver-dark)"/>
        <stop offset=".5" stop-color="var(--silver)"/>
        <stop offset="1" stop-color="var(--silver-dark)"/>
      </linearGradient>
    </defs>
    <rect x="0" y="20" width="500" height="2" fill="url(#silver)"/>
    <rect x="0" y="34" width="500" height="4" fill="url(#silver)"/>
    <rect x="0" y="256" width="500" height="4" fill="url(#silver)"/>
    <rect x="0" y="272" width="500" height="2" fill="url(#silver)"/>
  </svg>
  <div class="birds" role="img" aria-label="Faint flock of birds in flight"></div>
  <div class="brand">Colette's Studio</div>
  <div class="tagline">STUDIO · CAFE · GALLERY</div>
</section>

</body>
</html>
```